Golden Era Hollywood Movie Poster Design for a Wedding Invitation

We're looking for a movie poster designed along the lines of the styles of posters in the included "posters" file. We're thinking the "title" of the "movie" should be "The Wedding of the Year". This will be for a wedding invitation to the wedding of "Marla Quenstedder" and "Daniel Fenwoller", so their names should be featured as the "stars" of the movie. The wedding will take place at Pell Arrow Studios in Hollywood, so you can put on the poster "Presented by Pell Arrow Studios". The other uploaded files are photos of the bride and groom. You don't need to use any of the poses in those photos - we'd like to have a pose that's along the lines of the examples in the "posters" file - but I included the photos of the bride and groom as references to help you make the final poster look like them (but in the style of an old Hollywood movie poster). Make them look beautiful and glamorous like stars in a movie from Hollywood's golden era. :)

Reason: The designs we've received so far aren't quite giving exactly the old-Hollywood feel we're looking for, so we're giving one 5-day extension to see additional designs.

```html
<!DOCTYPE html>
<html lang="en">
<head>
<meta charset="utf-8">
<title>The Wedding of The Year</title>
<link rel="stylesheet" href="https://fonts.googleapis.com/css2?family=Kaushan+Script&family=Open+Sans:wght@400&family=Stint+Ultra+Condensed&display=swap">
<style>
  :root {
    --night: #0b0a1c;
    --violet-deep: #1e0c3a;
    --violet: #4a1a78;
    --violet-glow: #6b2aa0;
    --lilac-text: #dcd4f6;
    --star-light: #b7b0dc;
    --star-dark: #14102a;
    --portrait-hair: #3a2418;
    --portrait-skin: #b88470;
    --portrait-lilac: #8a78c4;
  }
  * { margin: 0; padding: 0; box-sizing: border-box; }
  html, body { width: 848px; height: 1200px; overflow: hidden; background: var(--night); }
  .poster {
    position: relative;
    width: 848px;
    height: 1200px;
    overflow: hidden;
    background:
      radial-gradient(ellipse 60% 45% at 45% 42%, var(--violet-glow) 0%, var(--violet) 35%, transparent 75%),
      radial-gradient(ellipse 70% 40% at 80% 5%, var(--violet) 0%, transparent 70%),
      linear-gradient(180deg, var(--violet-deep) 0%, #2a1050 45%, var(--night) 75%);
  }
  .poster__stars, .poster__portrait, .poster__skyline { position: absolute; left: 0; top: 0; }
  .cast {
    position: absolute;
    color: var(--lilac-text);
    font-family: "Stint Ultra Condensed", serif;
    text-align: center;
    line-height: 1;
  }
  .cast__first { display: block; font-size: 30px; }
  .cast__last { display: block; font-size: 56px; margin-top: 4px; }
  .cast--bride { left: 40px; top: 138px; width: 250px; }
  .cast--groom { left: 110px; top: 338px; width: 250px; }
  .cast__and { position: absolute; left: 168px; top: 258px; font-size: 36px; color: var(--lilac-text); font-family: "Stint Ultra Condensed", serif; }
  .presenter {
    position: absolute;
    left: 44px;
    top: 628px;
    width: 210px;
    text-align: center;
    font-family: "Open Sans", sans-serif;
    color: var(--lilac-text);
    line-height: 1.5;
  }
  .presenter__label { display: block; font-size: 16px; }
  .presenter__name { display: block; font-size: 19px; }
  .title {
    position: absolute;
    left: 0;
    top: 900px;
    width: 848px;
    font-family: "Kaushan Script", cursive;
    color: var(--lilac-text);
    font-weight: 400;
    line-height: 1;
  }
  .title__line { position: absolute; white-space: pre; font-size: 92px; }
  .title__line--one { left: 92px; top: 0; word-spacing: 60px; }
  .title__line--two { left: 140px; top: 90px; }
</style>
</head>
<body>
<main class="poster">
  <svg class="poster__stars" width="848" height="1200" viewBox="0 0 848 1200" aria-hidden="true">
    <defs>
      <polygon id="star" points="0,-10 2.9,-3.1 9.5,-3.1 4.2,1.2 5.9,8.1 0,4 -5.9,8.1 -4.2,1.2 -9.5,-3.1 -2.9,-3.1"/>
    </defs>
    <g fill="var(--star-light)" opacity="0.85">
      <use href="#star" transform="translate(25 32) scale(0.9)"/>
      <use href="#star" transform="translate(158 66) scale(0.8)"/>
      <use href="#star" transform="translate(480 76) scale(1.5)"/>
      <use href="#star" transform="translate(372 168) scale(1.1)"/>
      <use href="#star" transform="translate(540 146) scale(2.1)"/>
      <use href="#star" transform="translate(698 58) scale(2.7)"/>
    </g>
    <g fill="var(--star-dark)" opacity="0.85">
      <use href="#star" transform="translate(452 148) scale(2.4)"/>
      <use href="#star" transform="translate(744 82) scale(2.1)"/>
      <use href="#star" transform="translate(123 312) scale(2)"/>
      <use href="#star" transform="translate(255 268) scale(1)"/>
      <use href="#star" transform="translate(178 352) scale(1.1)"/>
      <use href="#star" transform="translate(134 412) scale(1.2)"/>
      <use href="#star" transform="translate(184 470) scale(1.4)"/>
      <use href="#star" transform="translate(180 548) scale(1.8)"/>
      <use href="#star" transform="translate(690 578) scale(1.3)"/>
    </g>
  </svg>

  <svg class="poster__portrait" width="848" height="1200" viewBox="0 0 848 1200" role="img" aria-label="Photograph of the bride and groom leaning in for a kiss, her long dark hair with lilac ends, his dark curly hair">
    <defs>
      <linearGradient id="portraitTone" x1="0" y1="0" x2="1" y2="1">
        <stop offset="0" stop-color="var(--portrait-hair)"/>
        <stop offset="0.35" stop-color="var(--portrait-skin)"/>
        <stop offset="0.6" stop-color="var(--portrait-lilac)"/>
        <stop offset="1" stop-color="var(--night)"/>
      </linearGradient>
    </defs>
    <path fill="url(#portraitTone)" opacity="0.9"
      d="M200 900 C180 720 190 520 240 400 C290 320 380 300 440 250 C500 170 600 150 700 170 C800 190 848 240 848 300 L848 900 Z"/>
  </svg>

  <svg class="poster__skyline" width="848" height="1200" viewBox="0 0 848 1200" aria-hidden="true">
    <path fill="var(--night)"
      d="M0 1200 L0 860 L40 800 L70 830 L85 740 L140 800 L175 830 L200 880 L240 810 L260 880 L320 800 L340 840 L380 790 L420 820 L460 860 L560 820 L600 740 L640 770 L700 740 L740 770 L790 720 L820 760 L848 740 L848 1200 Z"/>
  </svg>

  <p class="cast cast--bride">
    <span class="cast__first">Marla</span>
    <span class="cast__last">Quenstedder</span>
  </p>
  <span class="cast__and">&amp;</span>
  <p class="cast cast--groom">
    <span class="cast__first">Daniel</span>
    <span class="cast__last">Fenwoller</span>
  </p>

  <p class="presenter">
    <span class="presenter__label">Presented by</span>
    <span class="presenter__name">Pell Arrow Studios</span>
  </p>

  <h1 class="title">
    <span class="title__line title__line--one">“The Wedding</span>
    <span class="title__line title__line--two">of The Year”</span>
  </h1>
</main>
</body>
</html>
```